Harbourline construction company Business card design

I need a business card design for my company. I have a logo but dont have business cards with our logo..

www.harbourlineconstructco.com.au

The logo is on the website

I need the same details as this design I have attached. we have changed the logo and colours. just like the website

Industry/Entity Type

Building

```html
<!DOCTYPE html>
<html lang="en">
<head>
<meta charset="utf-8">
<title>Harbourline Construction – Business Card</title>
<link rel="stylesheet" href="https://fonts.googleapis.com/css2?family=Noto+Serif:wght@400;700&family=Arimo:wght@400&display=swap">
<style>
  :root {
    --page-bg: #e6e7e9;
    --card-white: #ffffff;
    --brand-blue: #2389c0;
    --brand-blue-dark: #1a6f9e;
    --grey-light: #d4d5d7;
    --grey-mid: #a9abae;
    --text-dark: #222428;
    --text-white: #ffffff;
    --photo-warm-1: #b88a63;
    --photo-warm-2: #e2d6c6;
    --photo-house-1: #c9bfae;
    --photo-house-2: #8f9a86;
  }
  html, body {
    margin: 0;
    padding: 0;
    width: 1200px;
    height: 802px;
    overflow: hidden;
    background: var(--page-bg);
  }
  .canvas {
    position: relative;
    width: 1200px;
    height: 802px;
  }
  .card {
    position: absolute;
    top: 251px;
    width: 540px;
    height: 300px;
    box-shadow: 0 10px 28px rgba(0,0,0,0.22);
    background: var(--card-white);
  }
  .card--front { left: 40px; }
  .card--back { left: 620px; }
  .card svg { display: block; }
  .brand-name {
    font-family: "Noto Serif", Georgia, serif;
    font-weight: 700;
    fill: var(--brand-blue-dark);
    letter-spacing: 1.5px;
  }
  .tagline {
    font-family: "Noto Serif", Georgia, serif;
    font-weight: 700;
    font-size: 17px;
    fill: var(--brand-blue);
  }
  .address {
    font-family: "Noto Serif", Georgia, serif;
    font-weight: 700;
    font-size: 15px;
    fill: var(--text-white);
  }
  .person-name {
    font-family: "Noto Serif", Georgia, serif;
    font-weight: 700;
    font-size: 17px;
    fill: var(--text-white);
  }
  .person-role {
    font-family: "Noto Serif", Georgia, serif;
    font-size: 13px;
    fill: var(--text-white);
  }
  .contact {
    font-family: "Arimo", Arial, sans-serif;
    font-size: 15px;
    fill: var(--text-dark);
  }
  .icon { fill: var(--brand-blue); }
</style>
</head>
<body>
<main class="canvas">

  <!-- Front of card -->
  <section class="card card--front" aria-label="Business card front">
    <svg width="540" height="300" viewBox="0 0 540 300">
      <defs>
        <linearGradient id="interiorTone" x1="0" y1="0" x2="1" y2="1">
          <stop offset="0" stop-color="var(--photo-warm-1)"/>
          <stop offset="1" stop-color="var(--photo-warm-2)"/>
        </linearGradient>
        <linearGradient id="greyFrontFill" x1="0" y1="0" x2="0" y2="1">
          <stop offset="0" stop-color="var(--grey-light)"/>
          <stop offset="1" stop-color="var(--grey-mid)"/>
        </linearGradient>
        <path id="taglineCurve" d="M0,158 C200,158 380,128 540,40"/>
      </defs>
      <rect class="photo-interior" role="img" aria-label="Photo of a finished home interior with timber floors" x="0" y="0" width="540" height="160" fill="url(#interiorTone)"/>
      <path class="wave-white" d="M0,120 C200,120 360,90 540,10 L540,300 L0,300 Z" fill="var(--card-white)"/>
      <path class="wave-blue" d="M0,200 C200,200 380,170 540,70 L540,96 C380,192 200,216 0,216 Z" fill="var(--brand-blue)"/>
      <path class="wave-grey" d="M0,216 C200,216 380,192 540,96 L540,300 L0,300 Z" fill="url(#greyFrontFill)"/>
      <text class="tagline" text-anchor="end"><textPath href="#taglineCurve" startOffset="95%">We build unique and beautiful homes</textPath></text>
      <rect class="brand-mark" x="30" y="150" width="14" height="14" fill="var(--brand-blue-dark)"/>
      <text class="brand-name" x="52" y="163" font-size="17">HARBOURLINE</text>
      <text class="brand-name" x="52" y="184" font-size="13">CONSTRUCTION</text>
      <text class="address" x="30" y="268">Unit 4 Level 2, 18 Tidewater Rd, Hillarys, WA 6025</text>
    </svg>
  </section>

  <!-- Back of card -->
  <section class="card card--back" aria-label="Business card back">
    <svg width="540" height="300" viewBox="0 0 540 300">
      <defs>
        <linearGradient id="houseTone" x1="0" y1="0" x2="1" y2="0">
          <stop offset="0" stop-color="#f4f4f2"/>
          <stop offset="0.35" stop-color="var(--photo-house-1)"/>
          <stop offset="1" stop-color="var(--photo-house-2)"/>
        </linearGradient>
        <linearGradient id="greyBackFill" x1="0" y1="0" x2="0" y2="1">
          <stop offset="0" stop-color="var(--grey-light)"/>
          <stop offset="1" stop-color="#c2c3c6"/>
        </linearGradient>
      </defs>
      <rect class="photo-house" role="img" aria-label="Photo of a two-storey family home with arched windows" x="0" y="0" width="540" height="300" fill="url(#houseTone)"/>
      <path class="band-top-grey" d="M0,0 H540 V82 C400,82 300,56 180,86 C100,106 40,126 0,136 Z" fill="var(--grey-light)" opacity="0.85"/>
      <path class="band-top-blue" d="M0,0 H540 V62 C400,62 300,40 180,68 C100,88 40,108 0,120 Z" fill="var(--brand-blue)"/>
      <text class="person-name" x="522" y="30" text-anchor="end">Marek Doyle</text>
      <text class="person-role" x="522" y="47" text-anchor="end">Director</text>
      <rect class="brand-mark" x="328" y="104" width="14" height="14" fill="var(--brand-blue-dark)"/>
      <text class="brand-name" x="350" y="117" font-size="17">HARBOURLINE</text>
      <text class="brand-name" x="350" y="137" font-size="13">CONSTRUCTION</text>
      <path class="wave-blue" d="M0,200 C150,184 330,194 540,136 L540,156 C330,216 150,206 0,222 Z" fill="var(--brand-blue)"/>
      <path class="wave-grey" d="M0,222 C150,206 330,216 540,156 L540,300 L0,300 Z" fill="url(#greyBackFill)"/>
      <g class="contact-email">
        <rect class="icon" x="326" y="196" width="14" height="10" rx="1"/>
        <path d="M326,196 L333,202 L340,196" fill="none" stroke="var(--card-white)" stroke-width="1.2"/>
        <text class="contact" x="350" y="206">harbourlineco@mail.com</text>
      </g>
      <g class="contact-phones">
        <rect class="icon" x="30" y="234" width="9" height="15" rx="2"/>
        <rect x="32" y="236" width="5" height="9" fill="var(--card-white)"/>
        <text class="contact" x="50" y="247">3571204466</text>
        <rect class="icon" x="28" y="255" width="14" height="4" rx="2"/>
        <rect class="icon" x="29" y="259" width="12" height="9" rx="2"/>
        <text class="contact" x="50" y="269">3879013352</text>
        <rect class="icon" x="29" y="281" width="12" height="9" rx="1"/>
        <rect x="31" y="283" width="8" height="3" fill="var(--card-white)"/>
        <text class="contact" x="50" y="291">3368207719</text>
      </g>
    </svg>
  </section>

</main>
</body>
</html>
```